Keys to business success

I love the principles of a book called "The quiet art of tending small gardens". I use the principles all the time at work. I'd like a poster made (map or web style design) to capture the books reminders. You can see a very basic verison of the design i'm looking for attached below "project summary".I've attached a word document of the text to include. Ive also attached two examples of the types of designs i'm looking for. The design will have to look modern and clear when printed on an 45.7 x 61 cm canvas.

Target Market(s)

Buisness people
Motivation

Industry/Entity Type

Business

Font styles to use
Serif

Requirements
Must have
• Web or map-like designs
• All 30 of the principles: 3 fonts (Title, sub-title and principles). The choice of fonts is up to the designer. No numbers for the principles.
• Professional feel
Nice to have
• Halos around phrases
Should not have
• No straight lines or ridgid concepts

```html
<!DOCTYPE html>
<html lang="en">
<head>
<meta charset="utf-8">
<title>Being a Leader – Principles Map</title>
<link rel="stylesheet" href="https://fonts.googleapis.com/css2?family=Tinos:wght@400;700&display=swap">
<style>
  :root {
    --bg-deep: #06222c;
    --bg-teal: #0f5a63;
    --bg-green: #1f7a5c;
    --bg-glow: #f3e6b0;
    --hub-top: #3aa0e6;
    --hub-bottom: #1565b5;
    --hub-ring: #ffffff;
    --link-blue: #2d8fe6;
    --link-orange: #ff5a1f;
    --text-light: #ffffff;
  }
  * { margin: 0; padding: 0; box-sizing: border-box; }
  html, body { width: 1200px; height: 899px; overflow: hidden; background: var(--bg-deep); }
  .poster {
    position: relative;
    width: 1200px;
    height: 899px;
    overflow: hidden;
    font-family: "Tinos", "Times New Roman", serif;
    color: var(--text-light);
  }
  .backdrop {
    position: absolute; inset: 0;
    background:
      radial-gradient(ellipse 260px 300px at 600px 250px, rgba(243,230,176,.75), rgba(243,230,176,0) 70%),
      radial-gradient(ellipse 420px 380px at 560px 520px, rgba(214,170,120,.45), rgba(214,170,120,0) 70%),
      radial-gradient(ellipse 500px 600px at 1050px 300px, rgba(170,210,220,.35), rgba(170,210,220,0) 70%),
      radial-gradient(ellipse 420px 420px at 150px 520px, rgba(60,160,90,.5), rgba(60,160,90,0) 70%),
      linear-gradient(135deg, var(--bg-teal) 0%, var(--bg-deep) 45%, var(--bg-green) 100%);
  }
  .links { position: absolute; inset: 0; }
  .links .branch { fill: none; stroke: var(--link-orange); stroke-width: 4; stroke-linecap: round; stroke-dasharray: 0 9; }
  .links .twig { fill: none; stroke: var(--link-blue); stroke-width: 3.4; stroke-linecap: round; stroke-dasharray: 0 8; }
  .hub-label {
    position: absolute;
    transform: translate(-50%, -50%);
    text-align: center;
    font-weight: 700;
    white-space: nowrap;
  }
  .hub-label--main { font-size: 40px; line-height: 48px; }
  .hub-label--topic { font-size: 20px; line-height: 27px; }
  .hub-label--like { font-size: 24px; line-height: 33px; }
  .principle {
    position: absolute;
    transform: translateX(-50%);
    text-align: center;
    white-space: nowrap;
    font-size: 15px;
    line-height: 21px;
    text-shadow: 0 0 4px rgba(0,0,0,.75), 0 0 2px rgba(0,0,0,.9);
  }
</style>
</head>
<body>
<main class="poster">
  <div class="backdrop" role="img" aria-label="Soft teal and green background photo of a businessman in a suit pointing upward with a glowing light burst behind the central circle"></div>

  <svg class="links" width="1200" height="899" viewBox="0 0 1200 899" aria-hidden="true">
    <defs>
      <linearGradient id="hubFill" x1="0" y1="0" x2="0" y2="1">
        <stop offset="0" stop-color="var(--hub-top)"/>
        <stop offset="1" stop-color="var(--hub-bottom)"/>
      </linearGradient>
    </defs>
    <path class="branch" d="M752 170 Q800 150 848 170"/>
    <path class="branch" d="M520 215 Q420 250 340 320"/>
    <path class="branch" d="M650 305 Q760 380 835 540"/>

    <path class="twig" d="M868 150 Q850 120 842 112"/>
    <path class="twig" d="M960 138 Q975 128 982 118"/>
    <path class="twig" d="M1010 180 Q1030 160 1050 155"/>
    <path class="twig" d="M1012 235 Q1030 245 1040 250"/>
    <path class="twig" d="M960 295 Q980 320 988 340"/>
    <path class="twig" d="M870 280 Q850 300 840 305"/>

    <path class="twig" d="M325 350 Q330 280 335 250"/>
    <path class="twig" d="M270 348 Q255 260 250 242"/>
    <path class="twig" d="M238 362 Q220 320 200 300"/>
    <path class="twig" d="M350 370 Q380 330 400 320"/>
    <path class="twig" d="M215 395 Q200 360 170 350"/>
    <path class="twig" d="M370 410 Q400 380 430 370"/>
    <path class="twig" d="M210 425 Q170 400 160 395"/>
    <path class="twig" d="M370 480 Q410 490 430 490"/>
    <path class="twig" d="M215 480 Q190 500 185 510"/>
    <path class="twig" d="M235 500 Q210 560 205 580"/>
    <path class="twig" d="M350 500 Q370 530 380 545"/>
    <path class="twig" d="M300 508 Q298 560 300 585"/>

    <path class="twig" d="M820 567 Q830 520 835 482"/>
    <path class="twig" d="M880 580 Q910 540 915 505"/>
    <path class="twig" d="M770 600 Q760 560 740 530"/>
    <path class="twig" d="M900 600 Q930 580 960 560"/>
    <path class="twig" d="M755 625 Q730 595 705 585"/>
    <path class="twig" d="M915 630 Q950 630 980 625"/>
    <path class="twig" d="M753 660 Q730 648 700 640"/>
    <path class="twig" d="M915 680 Q950 705 980 715"/>
    <path class="twig" d="M770 700 Q730 705 700 715"/>
    <path class="twig" d="M900 710 Q925 745 935 775"/>
    <path class="twig" d="M790 725 Q770 760 765 790"/>
    <path class="twig" d="M840 731 Q848 770 850 805"/>

    <circle cx="631" cy="202" r="104" fill="url(#hubFill)" stroke="var(--hub-ring)" stroke-width="5"/>
    <circle cx="930" cy="217" r="85" fill="url(#hubFill)" stroke="var(--hub-ring)" stroke-width="4"/>
    <circle cx="290" cy="425" r="82" fill="url(#hubFill)" stroke="var(--hub-ring)" stroke-width="4"/>
    <circle cx="835" cy="649" r="82" fill="url(#hubFill)" stroke="var(--hub-ring)" stroke-width="4"/>
  </svg>

  <h1 class="hub-label hub-label--main" style="left:631px;top:202px">BEING<br>A<br>LEADER</h1>
  <h2 class="hub-label hub-label--like" style="left:930px;top:217px">Making<br>People<br>Like<br>You</h2>
  <h2 class="hub-label hub-label--topic" style="left:290px;top:425px">Fundamental<br>Techniques<br>in<br>Handling<br>People</h2>
  <h2 class="hub-label hub-label--topic" style="left:835px;top:649px">Win People<br>to<br>Your Way<br>of<br>Thinking</h2>

  <p class="principle" style="left:832px;top:50px">Talk In Terms<br>Of The Other<br>Person's Interests</p>
  <p class="principle" style="left:1002px;top:30px">Be A Good Listener.<br>Encourage Others<br>To Talk<br>About Themselves</p>
  <p class="principle" style="left:1075px;top:141px">Smile</p>
  <p class="principle" style="left:1112px;top:192px">A Person's Name<br>Is To That Person<br>The Sweetest<br>And Most<br>Important Sound</p>
  <p class="principle" style="left:815px;top:306px">Become Genuinely<br>Interested<br>In<br>Other People</p>
  <p class="principle" style="left:1016px;top:347px">Make The Other<br>Person Feel Important<br>- And Do It Sincerely</p>

  <p class="principle" style="left:355px;top:184px">Begin With Praise<br>And Honest<br>Appreciation</p>
  <p class="principle" style="left:217px;top:197px">Don't Criticize,<br>Condemn or Complain</p>
  <p class="principle" style="left:153px;top:254px">Let The Other<br>Person Save Face</p>
  <p class="principle" style="left:451px;top:256px">Arouse In The<br>Other Person<br>An Eager Want</p>
  <p class="principle" style="left:115px;top:311px">Call Attention<br>To People's<br>Mistakes Indirectly</p>
  <p class="principle" style="left:505px;top:336px">Make The Other<br>Person Happy<br>About Doing<br>The Thing<br>You Suggest</p>
  <p class="principle" style="left:117px;top:394px">Talk About Your<br>Own Mistakes Before<br>Criticizing The<br>Other Person</p>
  <p class="principle" style="left:509px;top:459px">Praise The Slightest<br>Improvement<br>And Praise<br>Every Improvement.</p>
  <p class="principle" style="left:138px;top:488px">Give Honest,<br>Sincere,<br>Appreciation</p>
  <p class="principle" style="left:147px;top:560px">Use Encouragement.<br>Make The Fault<br>Seem Easy To Correct</p>
  <p class="principle" style="left:428px;top:553px">Give The Other<br>Person A<br>Fine Reputation<br>To Live Up To</p>
  <p class="principle" style="left:308px;top:588px">Ask Questions<br>Instead Of Giving<br>Direct Orders</p>

  <p class="principle" style="left:836px;top:412px">Throw<br>Down A<br>Challenge</p>
  <p class="principle" style="left:929px;top:440px">Dramatize<br>Your<br>Ideas</p>
  <p class="principle" style="left:726px;top:442px">The Only Way<br>To Get<br>The Best Of An<br>Argument Is To Avoid It</p>
  <p class="principle" style="left:1040px;top:481px">Show Respect For<br>The Other Person's<br>Opinion. Never Say,<br>"You're Wrong."</p>
  <p class="principle" style="left:651px;top:540px">Appeal To<br>The<br>Nobler Motives</p>
  <p class="principle" style="left:1058px;top:580px">Be Sympathetic<br>With The Other<br>Person's Ideas<br>And Desires</p>
  <p class="principle" style="left:636px;top:614px">If You Are Wrong<br>Admit It<br>Quickly<br>And<br>Emphatically</p>
  <p class="principle" style="left:1061px;top:679px">Try Honestly<br>To See Things<br>From The Other<br>Person's Point Of View</p>
  <p class="principle" style="left:647px;top:728px">Begin In<br>A Friendly<br>Manner</p>
  <p class="principle" style="left:1012px;top:778px">Let The Other Person<br>Feel That The Idea<br>Is His Or Hers</p>
  <p class="principle" style="left:741px;top:799px">Get The Other<br>Person Saying<br>"Yes, Yes"</p>
  <p class="principle" style="left:869px;top:812px">Let The Other<br>Person Do A Great<br>Deal Of The Talking</p>
</main>
</body>
</html>
```